Business card design needed

Business Card design required for new small plumbing business.
Would like a logo/text look that is simple and unique and does not have to be representative of a plumbing company (ie. having a cartoon plumber or toilet etc) as the companyname is self explanatory.
Would like the main colour to be green (lime green).
Updates

Industry/Entity Type

Plumber

Contact Information for Business Card

BRAVELL PLUMBING
ABN 61 904 127 558 003

Trevor Hasketh
Licensed Plumber 83615
Phone: 0412 870 245

27 Bravell Drive,
Ferncliff. 3984 Westland

Email: bravellplumbing@mailnest.example

Logo Text

Bravell Plumbing

Logo styles of interest
Character Logo
Wordmark Logo
Lettermark Logo

```html
<!DOCTYPE html>
<html lang="en">
<head>
<meta charset="utf-8">
<title>Bravell Plumbing – Business Card</title>
<link rel="stylesheet" href="https://fonts.googleapis.com/css2?family=Source+Sans+3:wght@400;600;700&display=swap">
<style>
  :root {
    --lime: #b7d766;
    --white: #ffffff;
    --card-edge: #c8c8c8;
    --page: #ffffff;
  }
  * { box-sizing: border-box; margin: 0; padding: 0; }
  html, body {
    width: 1200px; height: 559px; overflow: hidden;
    background: var(--page);
    font-family: "Source Sans 3", sans-serif;
  }
  .canvas { position: relative; width: 1200px; height: 559px; }

  .card {
    position: absolute; top: 133px;
    width: 509px; height: 294px;
    border: 1px solid var(--card-edge);
    background: var(--white);
    overflow: hidden;
  }
  .card--front { left: 76px; }
  .card--back { left: 615px; }

  .brand__square { position: absolute; background: var(--lime); }
  .brand__name {
    position: absolute; color: var(--lime); font-weight: 600;
    line-height: 1; white-space: nowrap;
  }

  .card--front .brand__square { left: 89px; top: 130px; width: 40px; height: 40px; }
  .card--front .brand__name { left: 135px; top: 144px; font-size: 34px; letter-spacing: -0.6px; }

  .card--back .brand__square { left: 32px; top: 48px; width: 18px; height: 18px; }
  .card--back .brand__name { left: 56px; top: 49px; font-size: 19.5px; letter-spacing: -0.2px; }

  .details {
    position: absolute; left: 32px; top: 89px; right: 0; bottom: 0;
    background: var(--lime); color: var(--white);
    text-align: right;
  }
  .details__name { position: absolute; right: 29px; top: 22px; font-size: 36px; font-weight: 700; line-height: 1; white-space: nowrap; }
  .details__role { position: absolute; right: 29px; top: 67px; font-size: 15px; font-weight: 400; white-space: nowrap; }
  .details__contact { position: absolute; right: 29px; top: 94px; font-size: 16px; font-weight: 700; line-height: 19px; white-space: nowrap; }
  .details__address { position: absolute; right: 29px; top: 145px; font-size: 15px; font-weight: 400; line-height: 18px; white-space: nowrap; }
</style>
</head>
<body>
<main class="canvas">
  <section class="card card--front" aria-label="Card front">
    <span class="brand__square"></span>
    <span class="brand__name">BRAVELL PLUMBING</span>
  </section>

  <section class="card card--back" aria-label="Card back">
    <span class="brand__square"></span>
    <span class="brand__name">BRAVELL PLUMBING</span>
    <div class="details">
      <p class="details__name">Trevor Hasketh</p>
      <p class="details__role">-&nbsp; Licensed Plumber</p>
      <p class="details__contact">0412 870 245 27 83615<br>bravellplumbing@mailnest.example</p>
      <p class="details__address">Bravell Drive, Ferncliff. 3984 Westland<br>ABN 61 904 127 558 003</p>
    </div>
  </section>
</main>
</body>
</html>
```